Allergy Social Media Advertising Graphics Needed

We already have the copy written for KT and Vistaloop ads and need a designer to ad a graphic element to the campaign.

Target Market(s)

Mostly soccer moms, suburban Washington, DC, highly educated, smart and research oriented.

Font styles to use
Sans Serif

Requirements
Must have
• An eye-catching concept that makes people stop scrolling and pay attention to the advertisement.
Nice to have
• Clean and simple design. Bold approach with an elegant feel.
Should not have
• Too busy or cartoon-like designs.

```html
<!DOCTYPE html>
<html lang="en">
<head>
<meta charset="utf-8">
<title>KT and Vistaloop Ads — Halden Allergy</title>
<link rel="stylesheet" href="https://fonts.googleapis.com/css2?family=Roboto:wght@400;500;700;900&display=swap">
<style>
  :root {
    --brand-blue: #0a5fa3;
    --deep-purple: #3b2a6b;
    --accent-blue: #11569c;
    --text-blue: #1b4f95;
    --white: #ffffff;
    --photo-light: #e9eef2;
    --photo-mid: #c9b3a0;
    --photo-teal: #5fb3a8;
  }
  * { box-sizing: border-box; margin: 0; padding: 0; }
  html, body { width: 1200px; height: 593px; overflow: hidden; background: var(--white); }
  body { font-family: "Roboto", Arial, sans-serif; position: relative; }

  .board-panel {
    position: absolute; left: 0; top: 0; width: 570px; height: 593px;
    background: var(--brand-blue); border-bottom-right-radius: 6px; border-top-right-radius: 6px;
  }
  .board-title {
    position: absolute; left: 0; top: 68px; width: 1200px; text-align: center;
    font-weight: 700; font-size: 37px; letter-spacing: 0.5px;
    background: linear-gradient(90deg, var(--white) 570px, var(--brand-blue) 570px);
    -webkit-background-clip: text; background-clip: text; color: transparent;
  }

  .ad {
    position: absolute; top: 139px; height: 314px; background: var(--white);
    overflow: hidden; box-shadow: 0 10px 18px rgba(0,0,0,0.35);
  }
  .ad--wide { left: 120px; width: 600px; }
  .ad--square { left: 757px; width: 321px; }
  .ad-art { position: absolute; inset: 0; }

  .ad-copy { position: absolute; top: 0; text-align: center; color: var(--text-blue); }
  .ad--wide .ad-copy { left: 400px; width: 200px; }
  .ad--square .ad-copy { left: 205px; width: 116px; }

  .brand-name {
    display: block; color: var(--deep-purple); font-weight: 400; line-height: 0.95; text-align: left;
  }
  .ad--wide .brand-name { margin: 17px 0 0 84px; font-size: 19px; }
  .ad--square .brand-name { margin: 22px 0 0 48px; font-size: 10.5px; }

  .headline { font-weight: 500; text-transform: uppercase; }
  .ad--wide .headline { margin-top: 38px; font-size: 11.5px; line-height: 14px; }
  .ad--square .headline { margin-top: 75px; font-size: 6.4px; line-height: 7.8px; }

  .offer { font-weight: 500; color: var(--deep-purple); text-transform: uppercase; }
  .offer strong { font-weight: 900; color: var(--accent-blue); }
  .ad--wide .offer { margin-top: 25px; font-size: 15px; line-height: 17.5px; }
  .ad--square .offer { margin-top: 13px; font-size: 8px; line-height: 9.6px; }

  .cta {
    display: inline-block; background: var(--deep-purple); color: var(--white);
    font-weight: 500; border-radius: 20px; text-transform: uppercase;
  }
  .ad--wide .cta { margin-top: 40px; width: 106px; height: 25px; line-height: 25px; font-size: 10px; }
  .ad--square .cta { margin-top: 21px; width: 59px; height: 13px; line-height: 13px; font-size: 5.3px; }

  .social-row { display: flex; justify-content: center; }
  .social-dot { border-radius: 50%; background: var(--deep-purple); }
  .ad--wide .social-row { margin-top: 46px; gap: 10px; }
  .ad--wide .social-dot { width: 10px; height: 10px; }
  .ad--square .social-row { margin-top: 38px; gap: 6px; }
  .ad--square .social-dot { width: 5px; height: 5px; }
</style>
</head>
<body>
  <div class="board-panel"></div>
  <h1 class="board-title">KT AND VISTALOOP ADS</h1>

  <section class="ad ad--wide">
    <svg class="ad-art" width="600" height="314" viewBox="0 0 600 314">
      <defs>
        <linearGradient id="wide-photo" x1="0" y1="0" x2="1" y2="1">
          <stop offset="0" stop-color="#eef2f5"/>
          <stop offset="0.45" stop-color="#d8c2ae"/>
          <stop offset="0.8" stop-color="#b98f6e"/>
          <stop offset="1" stop-color="#5fb3a8"/>
        </linearGradient>
      </defs>
      <path role="img" aria-label="Photo of a smiling young girl at a family breakfast table"
            d="M0 0 H316 Q400 150 322 314 H0 Z" fill="url(#wide-photo)"/>
      <path d="M20 0 Q0 140 15 140" fill="none" stroke="#3b2a6b" stroke-width="5"/>
      <path d="M316 0 Q400 150 322 314" fill="none" stroke="#0a5fa3" stroke-width="8"/>
      <path d="M350 0 Q392 70 390 106" fill="none" stroke="#3b2a6b" stroke-width="4"/>
      <path d="M394 184 Q392 260 350 314" fill="none" stroke="#3b2a6b" stroke-width="4"/>
      <path d="M320 100 Q335 230 258 314" fill="none" stroke="#3b2a6b" stroke-width="9"/>
    </svg>
    <div class="ad-copy">
      <span class="brand-name">halden<br>allergy</span>
      <p class="headline">Is worrying about your<br>child’s peanut allergy<br>driving you nuts?</p>
      <p class="offer">Oral <strong>Immunotherapy</strong><br>could <strong>help</strong>.</p>
      <a class="cta">Learn more.</a>
      <div class="social-row"><span class="social-dot"></span><span class="social-dot"></span><span class="social-dot"></span><span class="social-dot"></span></div>
    </div>
  </section>

  <section class="ad ad--square">
    <svg class="ad-art" width="321" height="314" viewBox="0 0 321 314">
      <defs>
        <linearGradient id="square-photo" x1="0" y1="0" x2="1" y2="1">
          <stop offset="0" stop-color="#e9e4df"/>
          <stop offset="0.45" stop-color="#d4b9a2"/>
          <stop offset="0.8" stop-color="#b48b6c"/>
          <stop offset="1" stop-color="#5fb3a8"/>
        </linearGradient>
      </defs>
      <path role="img" aria-label="Close-up photo of a smiling young girl with her mother at breakfast"
            d="M0 0 H140 Q215 140 142 314 H0 Z" fill="url(#square-photo)"/>
      <path d="M140 0 Q215 140 142 314" fill="none" stroke="#0a5fa3" stroke-width="7"/>
      <path d="M170 0 Q210 60 212 105" fill="none" stroke="#3b2a6b" stroke-width="3"/>
      <path d="M214 180 Q210 260 168 314" fill="none" stroke="#3b2a6b" stroke-width="3"/>
      <path d="M150 90 Q175 230 90 314" fill="none" stroke="#3b2a6b" stroke-width="8"/>
    </svg>
    <div class="ad-copy">
      <span class="brand-name">halden<br>allergy</span>
      <p class="headline">Is worrying about your<br>child’s peanut allergy<br>driving you nuts?</p>
      <p class="offer">Oral <strong>Immunotherapy</strong><br>could <strong>help</strong>.</p>
      <a class="cta">Learn more.</a>
      <div class="social-row"><span class="social-dot"></span><span class="social-dot"></span><span class="social-dot"></span><span class="social-dot"></span></div>
    </div>
  </section>
</body>
</html>
```